Lakeshore Clinical Allies Business Flyers

I am in need of a nice, professional brochure that I can leave behind with my clients. I have template built, but will need a new design that I can be proud of and that I can have the template to update and change down the road. I will want to reflect my medical distribution services in the form of Labs I partner with (Genetic Testing and Pathology) and Pharmacies I partner with for Topical solutions (creams for commercial and medicare) as well as worker's compensation. Finally, I have toxicology testing.

Target Market(s)

Medical clinics, physicians

Industry/Entity Type

Medical

Font styles to use
Other font styles liked:
• see brochure (Avenir Next) NOTE: Feel free to use another font if you think it is more elegant and/or a better option

Colors
000000
cbcbcb
f7f7f7

Requirements
Must have
• Focus on my brand (trusted partner) showcase the logo (carbon fiber look on all black areas) See the bottom right of the brochure I uploaded. On the inside, I want to feature my labs and pharmacy(s). I will send you the link to them so you can use items from their websites. We are focusing on PROFESSIONAL and TRUSTED service with strong partnerships with world class labs, etc.
• Focus on we handle all the billing and collection processes. All of our partners are chosen because they have your patient satisfaction in mind as a top priority. We are always on the "right side" of insurance and are HIPPA compliant and have a zero tolerance for non-compliance.
• What we do: Testing (Toxicology and Genetic Testing) Pharmacogenetics studies how genetic various impact the way our bodies respond to certain medications. By having detailed patient data, physicians can now practice precise, individualized, tailored treatment programs based on personal date of each patient.
Nice to have
• Note the importance of the "mirroring/reflection" in my logo on the "P" and the "carbon fiber" look and feel on the black "M". if you can build that into the look and feel of the brochure, it would help to "pop" the brand and my logo.
• Build the partner labs/pharmacy into the brochure for credibility. ( I would say some of our key partners and leave it opened ended like we have many more)
• Topical Solutions: www.curavexallies.example (innovation/innovative medicare and commercial insurance solutions
• www.brindlecaremed.example (workers comp solutions)
• Labs:
• www.zenthoraassaylabs.example
• www.pellucigenomics.example
• I will provide more content and verbiage if needed, but much of it you can get from the website. The key is that we do all the billing, we supply all the materials including paperwork, forms, collection kits and all shipping. We differentiate ourselves by taking all the cumbersome work away from the staff through automation and best practices, topped off by personal/customized service.
Should not have
• Cluttered and busy...not many colors that create confusion and/or attention span issues.

```html
<!DOCTYPE html>
<html lang="en">
<head>
<meta charset="utf-8">
<title>Lakeshore Clinical Allies – Brochure Inside</title>
<link href="https://fonts.googleapis.com/css2?family=Mulish:wght@400;500;600;700;800&display=swap" rel="stylesheet">
<style>
:root{
  --stage:#a6a8ab;
  --paper:#eeeeef;
  --ink:#1b1b1b;
  --body:#333333;
  --black:#000000;
  --band:#1c1c1c;
  --white:#ffffff;
  --soft:#cbcbcb;
}
*{box-sizing:border-box;margin:0;padding:0}
html,body{width:1200px;height:931px;overflow:hidden}
body{background:var(--stage);font-family:"Mulish",sans-serif;color:var(--body);position:relative}
.panel{position:absolute;top:38px;height:854px;width:369px;overflow:hidden}
.panel-left{left:52px;width:367px;background:var(--paper)}
.panel-middle{left:419px;background:var(--black);color:var(--white)}
.panel-right{left:788px;background:var(--paper)}
.base-band{position:absolute;left:0;right:0;bottom:0;height:22px;background:linear-gradient(#2b2b2b,#0d0d0d)}
.photo{position:absolute;display:block}
.panel-title{position:absolute;font-size:22px;font-weight:700;color:var(--ink);letter-spacing:.2px}
.block{position:absolute;left:26px;right:20px;font-size:12px;line-height:15px;text-align:justify}
.block h3{font-size:16px;font-weight:700;color:var(--ink);line-height:18px}
.block h4{font-size:13px;font-weight:700;color:var(--ink);line-height:16px}
.thumb{float:left;width:60px;height:60px;border-radius:50%;margin:2px 9px 4px 0}
/* middle */
.panel-middle .panel-title{color:var(--white)}
.svc{position:absolute;left:39px;right:16px;font-size:13.4px;line-height:16.7px;font-weight:400}
.svc h3{font-size:16.5px;font-weight:600;line-height:20px}
.svc ul{list-style:disc;padding-left:15px}
.svc ul ul{list-style:circle;padding-left:19px}
/* right */
.block-right{position:absolute;left:22px;right:26px;font-size:12px;line-height:15px;text-align:justify}
.block-right h3{font-size:15px;font-weight:700;color:var(--ink);line-height:20px;margin-bottom:3px}
.logo-row{position:absolute;left:22px;right:20px;display:flex;justify-content:space-between;align-items:center}
.partner-name{display:flex;align-items:center;gap:5px;font-size:11.5px;font-weight:600;color:#3a3a3a}
.partner-name i{display:inline-block;width:10px;height:10px;border-radius:50%;background:#555}
.quote{position:absolute;left:22px;right:26px;font-size:10.5px;line-height:13.3px;text-align:justify}
.quote .thumb{width:50px;height:50px;margin:0 10px 4px 0}
.quote cite{display:block;font-style:italic;text-align:left}
</style>
</head>
<body>

<section class="panel panel-left">
  <div class="photo" role="img" aria-label="Scientist working at a laboratory bench" style="left:0;top:0;width:367px;height:120px;background:linear-gradient(120deg,#6d7f94,#c9d3dd 55%,#8e9aa8)"></div>
  <div class="photo" role="img" aria-label="Photo card of medical instruments" style="left:213px;top:92px;width:66px;height:72px;background:linear-gradient(#cfd8e0,#8a97a3);border:3px solid var(--white);transform:rotate(-8deg)"></div>
  <div class="photo" role="img" aria-label="Photo card of pharmacy shelves" style="left:278px;top:90px;width:70px;height:66px;background:linear-gradient(#d9dfe4,#9aa7b1);border:3px solid var(--white);transform:rotate(7deg)"></div>
  <h2 class="panel-title" style="left:31px;top:137px">WHAT WE DO:</h2>

  <div class="block" style="top:180px">
    <div class="thumb" role="img" aria-label="Pipette dropping sample into test tubes" style="background:radial-gradient(circle at 40% 40%,#e8eef4,#7fa1c3)"></div>
    <h3 style="margin-left:69px">TESTING</h3>
    <h4>Genetics</h4>
    Our testing partners help to empower every medical professional and patient with the specific knowledge to properly prescribe and dose a patient’s symptoms and conditions with accurate medication in specific dosages for optimized results. All of this can be done by providing genetic information specific to the patient and the condition to be treated.
  </div>

  <div class="block" style="top:339px">
    <h4>Pathology</h4>
    Our partner pathology laboratory is dedicated to bringing quality anatomic pathology services to Urologists, Gastroenterologists, Dermatologists, Neurologists, Pain Management Specialists and Podiatrists.
  </div>

  <div class="block" style="top:432px">
    <div class="thumb" role="img" aria-label="Topical cream on a fingertip" style="background:radial-gradient(circle at 50% 45%,#f3efe9,#8a5c4a)"></div>
    <h3>TOPICALS</h3>
    Our topically applied specialty products are manufactured, FDA-approved, and often covered by most insurance prescription plans. These products can be used to treat a variety of conditions including acute to chronic pain. We are also your partner for personalized medications that are made just for you! Like the professional physicians and providers we serve, we believe that a patient should be treated as a unique individual, and not as just another statistic and that the best-case scenario is when a patient, a medical provider, and a pharmacy work together to come up with the best possible treatment plan.
  </div>

  <div class="block" style="top:654px">
    <div class="thumb" role="img" aria-label="Gloved hand holding a sample vial" style="background:radial-gradient(circle at 45% 45%,#e9eef5,#3f6fb0 60%,#b3323a)"></div>
    <h3>TOXICOLOGY</h3>
    Our labs offer comprehensive urine and saliva tox screening. Too often, because of the difficulty with monitoring and documenting patients’ compliance, many healthcare providers are reluctant to offer adequate pain management. Most importantly, our lab employees care deeply for our providers and patients and work tirelessly to deliver world class turnaround times and outstanding, easy to read and understand results, including normalized reports for toxicology.
  </div>
  <div class="base-band"></div>
</section>

<section class="panel panel-middle">
  <h2 class="panel-title" style="left:39px;top:32px">OUR SERVICES:</h2>
  <div class="svc" style="top:62px">
    <h3>Genetic Testing</h3>
    <ul>
      <li>Hereditary Cancer</li>
      <li>Inherited Conditions</li>
      <li>Pharmacogenetics (Drug Metabolism)</li>
      <li>Preconception &amp; Pregnancy</li>
    </ul>
  </div>
  <div class="svc" style="top:162px">
    <h3>Pathology</h3>
    <ul>
      <li>Client Bill Programs</li>
      <li>Dermatology</li>
      <li>Epidermal Nerve Fiber Density (ENFD)</li>
      <li>Gastroenterology (General Biopsies)
        <ul>
          <li>Micro colitis</li>
          <li>EGD (Barrett’s, metaplasia, gastric carcinoma, celiac, etc.</li>
          <li>HER2/neu testing by IHC &amp; FISH for every gastric &amp; esophageal cancer</li>
          <li>Microsatellite instability testing for every colon cancer</li>
          <li>Special stand for H.pylori on every gastric biopsy</li>
        </ul>
      </li>
      <li>“Lean Lab” In-House Laboratory for Group Practices</li>
      <li>Podiatry
        <ul>
          <li>Biopsy and PAS (ie, histopathology)</li>
          <li>Skin Lesions/pigmented lesions/Nevi</li>
          <li>Plantar Warts</li>
          <li>Amputated toes</li>
          <li>Wound Debridement Tissue</li>
          <li>Soft Tissue Lesions/Tumors (neuroma)</li>
          <li>Bone Shaving</li>
          <li>Nail (Onychomycosis)</li>
        </ul>
      </li>
      <li>Urology
        <ul><li>Prostate (needle core biopsies)</li></ul>
      </li>
    </ul>
  </div>
  <h2 class="panel-title" style="left:34px;top:635px">WHO WE SERVICE:</h2>
  <div class="svc" style="top:670px">
    <ul>
      <li>Dermatology</li>
      <li>Family Practice</li>
      <li>Gastroenterology</li>
      <li>Mental Health</li>
      <li>Obstetrics and Gynecology</li>
      <li>Orthopedic and Sports Medicine</li>
      <li>Pain Management</li>
      <li>Physiatry</li>
      <li>Podiatry</li>
      <li>Urology</li>
    </ul>
  </div>
</section>

<section class="panel panel-right">
  <div class="photo" role="img" aria-label="Doctor shaking hands with a colleague" style="left:0;top:0;width:369px;height:120px;background:linear-gradient(110deg,#b9c3cf,#e8ecf0 50%,#9ba6b2)"></div>
  <div class="photo" role="img" aria-label="Photo card of a health insurance form with stethoscope" style="left:250px;top:96px;width:108px;height:86px;background:linear-gradient(#e6e6e6,#8f8f8f);border:3px solid var(--white);transform:rotate(9deg)"></div>
  <h2 class="panel-title" style="left:19px;top:135px">OUR PARTNERS:</h2>

  <div class="block-right" style="top:176px">
    <h3>Labs</h3>
    All of our Lab Partners offer full spectrum testing and are CLIA certified and CAP accredited. We offer personalized support and paperless reporting via online portals and EMR integration.
  </div>
  <div class="logo-row" style="top:284px">
    <span class="partner-name"><i></i>Pelluci Genomics</span>
    <span class="partner-name">Zenthora Assay Labs</span>
    <span class="partner-name">Corvane Pathology</span>
  </div>

  <div class="block-right" style="top:331px">
    <h3>Pharmacies</h3>
    Lakeshore Clinical Allies bridges the gap between manufacturers and patients through our network of pharmacies that take care of everything for your valued patient from processing insurance, to ensuring delivery of the script straight to your patient's home.
  </div>
  <div class="logo-row" style="top:455px">
    <span class="partner-name"><i></i>Orrin Specialty Rx</span>
    <span class="partner-name">Curavex Allies</span>
    <span class="partner-name">Brindle Care Medical</span>
  </div>

  <h2 class="panel-title" style="left:22px;top:508px">REFERENCE</h2>
  <div class="quote" style="top:544px">
    <div class="thumb" role="img" aria-label="Clinic emblem" style="background:var(--white);border:1px solid var(--soft)"></div>
    I have been working with Daniel and his team for over a year and we’ve been extremely impressed with his services and in particular, his attention to detail. Lakeshore Clinical Products and the labs and pharmacies they partner with provide our clinic great value and service. Our physicians and patients have been extremely satisfied with Daniel, especially his personal touch. We consider them as our partner and not just a vendor.
    <cite>Marcus Delane, Riverbend Medical Associates</cite>
  </div>
  <div class="quote" style="top:697px">
    <div class="thumb" role="img" aria-label="Portrait of a physician" style="background:radial-gradient(circle,#f4f4f4,#b7b7b7 70%,#7a1f2b)"></div>
    Daniel’s team and network of providers is simply the best we’ve worked with and we truly value our relationship. Rest assured, anything that needs to be taken care of from start to finish will be done professionally and with precision. I highly recommend that you consider working with Lakeshore Clinical Allies as a solutions provider for your lab and pharmacy needs.
    <cite>Dr. Alan Whitcombe, Cedar Hollow Pain Specialists</cite>
  </div>
  <div class="base-band"></div>
</section>

</body>
</html>
```